Business Card for Used Machinery Dealer
Brelton-Sakowitz, Evan Tolliver
Business Card for Used Machinery Dealer - Manufacturing
Creative Brief
Use standard fonts
Designer may use whatever fonts they see fit
Professional
Warren Tolliver
President
7819 E. 142nd St. Maple Hollow IL 60917
warrentollivrxq@mailnest-example.com
www.breltonsakowitz-example.com
Feel free to think out of the box. The color of the card stock may be white, or may be something else. We are open to using glossy or matted. The card stock should probably be a little thick to give it some extra presence. Try different fonts. Maybe the same as the logo would be good maybe something different
If the designer has a great idea for the back of a card I am open to looking at it. Likely the back of the card would consist of our email address. www.breltonsakowitz-example.com

```html
<!DOCTYPE html>
<html lang="en">
<head>
<meta charset="utf-8">
<title>Brelton-Sakowitz Stationery</title>
<link href="https://fonts.googleapis.com/css2?family=Roboto+Condensed:wght@400;700&family=Roboto:wght@400;700&display=swap" rel="stylesheet">
<style>
  :root {
    --blue: #1f6fc4;
    --blue-deep: #0d4c9a;
    --blue-light: #3a8fe0;
    --orange: #f2731d;
    --paper: #ffffff;
    --ink: #333a44;
    --muted: #6b7380;
    --stage: #ffffff;
    --edge: #d6d9de;
  }
  * { margin: 0; padding: 0; box-sizing: border-box; }
  html, body { width: 1200px; height: 681px; overflow: hidden; background: var(--stage); }
  body { position: relative; font-family: "Roboto", Arial, sans-serif; color: var(--ink); }

  .sheet {
    position: absolute;
    background: var(--paper);
    border: 1px solid var(--edge);
    box-shadow: 3px 4px 8px rgba(0,0,0,0.22);
    overflow: hidden;
  }
  .header-band { position: absolute; left: 0; top: 0; width: 100%; display: block; }

  .brand { position: absolute; display: flex; flex-direction: column; }
  .brand-row { display: flex; align-items: center; gap: 6px; }
  .brand-dot { border-radius: 50%; background: var(--blue); flex: none; }
  .brand-name {
    font-family: "Roboto Condensed", Arial, sans-serif;
    font-weight: 700; color: var(--blue); letter-spacing: 0.02em; white-space: nowrap;
  }
  .brand-tag {
    font-family: "Roboto Condensed", Arial, sans-serif;
    color: var(--muted); letter-spacing: 0.08em; white-space: nowrap;
  }

  /* Envelope front */
  .envelope-front { left: 67px; top: 103px; width: 389px; height: 190px; }
  .envelope-front .header-band { height: 52px; }
  .envelope-front .brand { left: 14px; top: 62px; }
  .envelope-front .brand-dot { width: 18px; height: 18px; }
  .envelope-front .brand-name { font-size: 15px; }
  .envelope-front .brand-tag { font-size: 5px; margin-top: 2px; }
  .envelope-front .return-address { position: absolute; left: 14px; top: 108px; font-size: 6.5px; color: var(--ink); }

  /* Envelope back */
  .envelope-back { left: 67px; top: 336px; width: 389px; height: 211px; }
  .envelope-back .flap { position: absolute; left: 0; top: 0; width: 100%; height: 60px; }
  .envelope-back .seal-mark { position: absolute; left: 50%; top: 100px; transform: translateX(-50%); display: flex; align-items: center; gap: 5px; }
  .envelope-back .brand-dot { width: 20px; height: 20px; }
  .envelope-back .brand-name { font-size: 10px; }

  /* Letterhead */
  .letterhead { left: 619px; top: 48px; width: 377px; height: 571px; }
  .letterhead .header-band { height: 74px; }
  .letterhead .brand { left: 22px; top: 90px; }
  .letterhead .brand-dot { width: 24px; height: 24px; }
  .letterhead .brand-name { font-size: 17px; }
  .letterhead .brand-tag { font-size: 5.5px; margin-top: 2px; }
  .letterhead .contact { position: absolute; left: 22px; top: 180px; font-size: 6.5px; line-height: 1.45; color: var(--ink); }

  /* Business card front */
  .card-front { left: 967px; top: 149px; width: 144px; height: 101px; }
  .card-front .header-band { height: 22px; }
  .card-front .brand { left: 7px; top: 28px; }
  .card-front .brand-dot { width: 12px; height: 12px; }
  .card-front .brand-name { font-size: 8px; }
  .card-front .brand-tag { font-size: 3px; margin-top: 1px; }
  .card-front .holder { position: absolute; right: 7px; top: 28px; text-align: left; width: 54px; font-size: 4.2px; line-height: 1.4; }
  .card-front .holder-name { font-size: 5px; font-weight: 700; color: var(--ink); }
  .card-front .holder-title { font-size: 4px; color: var(--muted); margin-bottom: 4px; }

  /* Business card back */
  .card-back { left: 967px; top: 278px; width: 144px; height: 101px; }
  .card-back .back-mark { position: absolute; left: 50%; top: 50%; transform: translate(-50%,-50%); display: flex; flex-direction: column; align-items: center; gap: 4px; }
  .card-back .brand-dot { width: 16px; height: 16px; }
  .card-back .brand-name { font-size: 6px; }
</style>
</head>
<body>

<svg width="0" height="0" style="position:absolute" aria-hidden="true">
  <defs>
    <linearGradient id="band-blue" x1="0" y1="0" x2="0" y2="1">
      <stop offset="0" stop-color="#0d4c9a"/>
      <stop offset="0.6" stop-color="#1f6fc4"/>
      <stop offset="1" stop-color="#3a8fe0"/>
    </linearGradient>
    <symbol id="header-wave" viewBox="0 0 400 60" preserveAspectRatio="none">
      <rect width="400" height="60" fill="url(#band-blue)"/>
      <path d="M0,60 L0,34 Q200,0 400,34 L400,60 Z" fill="#f2731d"/>
      <path d="M0,60 L0,46 Q200,10 400,46 L400,60 Z" fill="#ffffff"/>
    </symbol>
  </defs>
</svg>

<section class="sheet envelope-front">
  <svg class="header-band" preserveAspectRatio="none"><use href="#header-wave" width="100%" height="100%"/></svg>
  <div class="brand">
    <div class="brand-row"><span class="brand-dot"></span><span class="brand-name">BRELTON-SAKOWITZ</span></div>
    <span class="brand-tag">REMANUFACTURING | INTEGRATION | SALES</span>
  </div>
  <p class="return-address">7819 E. 142nd St. | Maple Hollow, IL 60917</p>
</section>

<section class="sheet envelope-back">
  <svg class="flap" viewBox="0 0 389 60" preserveAspectRatio="none">
    <path d="M0,0 L10,40 Q14,52 30,52 L359,52 Q375,52 379,40 L389,0" fill="none" stroke="#b9bec6" stroke-width="1"/>
  </svg>
  <div class="seal-mark">
    <span class="brand-dot"></span><span class="brand-name">BRELTON-SAKOWITZ</span>
  </div>
</section>

<section class="sheet letterhead">
  <svg class="header-band" preserveAspectRatio="none"><use href="#header-wave" width="100%" height="100%"/></svg>
  <div class="brand">
    <div class="brand-row"><span class="brand-dot"></span><span class="brand-name">BRELTON-SAKOWITZ</span></div>
    <span class="brand-tag">REMANUFACTURING | INTEGRATION | SALES</span>
  </div>
  <address class="contact" style="font-style:normal">
    7819 E. 142nd St.<br>
    Maple Hollow, IL 60917<br>
    Phone: (555) 014-2200<br>
    Fax: (555) 014-0103<br>
    Cell: (555) 017-3416<br>
    Email: warrentollivrxq@mailnest-example.com<br>
    www.breltonsakowitz-example.com
  </address>
</section>

<section class="sheet card-front">
  <svg class="header-band" preserveAspectRatio="none"><use href="#header-wave" width="100%" height="100%"/></svg>
  <div class="brand">
    <span class="brand-dot" style="margin-bottom:3px"></span>
    <span class="brand-name">BRELTON-SAKOWITZ</span>
    <span class="brand-tag">REMANUFACTURING | SALES</span>
  </div>
  <div class="holder">
    <div class="holder-name">Warren Tolliver</div>
    <div class="holder-title">President</div>
    7819 E. 142nd St.<br>
    Maple Hollow, IL 60917<br>
    P: (555) 014-2200<br>
    C: (555) 017-3416<br>
    www.breltonsakowitz-example.com
  </div>
</section>

<section class="sheet card-back">
  <div class="back-mark">
    <span class="brand-dot"></span>
    <span class="brand-name">BRELTON-SAKOWITZ</span>
  </div>
</section>

</body>
</html>
```